Elite boxing brochure

I need a brochure for a boxing training camp please. I would like it to look like the imagery on our Desmond Okafor website http://www.okaforfightcamp.com/ . I have attached some images and the text to be included. The final design needs to attract High net worth individuals, and communicate exclusivity. many thanks. Pete. Please feel free to copy any images from our Okafor website- we have the license to use any and all images on that site

```html
<!DOCTYPE html>
<html lang="en">
<head>
<meta charset="utf-8">
<title>Elite Boxing Camp – Back Cover</title>
<link rel="stylesheet" href="https://fonts.googleapis.com/css2?family=Fira+Sans:ital,wght@1,400;1,600;1,800&display=swap">
<style>
  :root {
    --stage: #d9d9d9;
    --red: #c8383d;
    --red-light: #d65458;
    --red-dark: #b52b31;
    --ink: #1c1c1c;
    --band: #2b2b2b;
    --band-fade: rgba(43, 43, 43, 0);
    --body-text: #6e1a1e;
    --white: #ffffff;
  }
  * { margin: 0; padding: 0; box-sizing: border-box; }
  html, body {
    width: 1200px;
    height: 800px;
    overflow: hidden;
    background: var(--stage);
    font-family: "Fira Sans", Arial, sans-serif;
  }
  .back-cover {
    position: absolute;
    left: 325px;
    top: 45px;
    width: 550px;
    height: 710px;
    overflow: hidden;
    background: linear-gradient(100deg, var(--red-dark) 0%, var(--red) 30%, var(--red-light) 55%, var(--red) 80%, var(--red-dark) 100%);
  }
  .intro {
    position: absolute;
    top: 74px;
    left: 100px;
    width: 350px;
    text-align: center;
  }
  .intro__title {
    color: var(--white);
    font-weight: 800;
    font-style: italic;
    font-size: 18px;
    margin-bottom: 6px;
  }
  .intro__text {
    color: var(--body-text);
    font-style: italic;
    font-weight: 400;
    font-size: 10.5px;
    line-height: 15.5px;
  }
  .texture-band {
    position: absolute;
    left: 0;
    top: 245px;
    width: 550px;
    height: 300px;
    background: linear-gradient(180deg, var(--band) 0%, var(--band) 52%, var(--band-fade) 100%);
  }
  .event-details {
    position: absolute;
    left: 100px;
    top: 300px;
    color: var(--white);
    font-weight: 800;
    font-style: italic;
    font-size: 17px;
    line-height: 1.1;
    list-style: none;
  }
  .contact {
    position: absolute;
    top: 556px;
    left: 0;
    width: 550px;
    text-align: center;
    color: var(--ink);
    font-style: italic;
    font-size: 11px;
    line-height: 1.5;
  }
  .contact__name { font-weight: 400; }
  .contact__name strong { font-weight: 600; }
  .contact__lines { font-weight: 600; font-style: normal; }
</style>
</head>
<body>
  <article class="back-cover">
    <section class="intro">
      <h2 class="intro__title">Who should come?</h2>
      <p class="intro__text">This is an ELITE boxing training camp designed to equip you with knowledge, the skills and a training program to improve massively over a 6 month period. We GUARRANTEE your improvement if you stick to the program AND eat healthy. You have an opportunity to work with the very best in the world so please be open minded and be prepared to learn. You should come if you want a structured, individualised program of improvement GUARANTEED to work for YOU.</p>
    </section>

    <div class="texture-band" role="img" aria-label="Dark torn grunge paint band across the page, breaking into splatter at its lower edge"></div>

    <ul class="event-details">
      <li>Date 16-18th April 2015</li>
      <li>Venue ( leave blank)</li>
      <li>Cost &nbsp;&nbsp;US $ 3000 per person</li>
    </ul>

    <footer class="contact">
      <p class="contact__name">Contact <strong>Mr Karim Haddad</strong></p>
      <p class="contact__lines">+971 50 123 4567 &nbsp;| email: &nbsp;karim@ringside-elite.com</p>
    </footer>
  </article>
</body>
</html>
```